Create a business Card for a Women Owned Business Body Positive Company. The winner we hope to work with on other projects coming up for grand opening for flyers, postcards, email marketing, facebook page, stationary, labels, tshirt design....
We would like if possible in the background of the card a infinity symbol or crown if it fits into the design if not it's ok. But I am open to all suggestions we had alot problems with the our new logo being created this time sad to say :(

Our colors are Royal Purple, Grey, Black Thank you in advance for your talent, you hard work and your submissions!
Delia and Nadine :)
Updates

my Logo is velvet harbor boutique which is purple and has a heart and infinity sign in it and my colors are purple silver and black only of another card i had done nothing else. My logo is VELVET HARBOR BOUTIQUE LOGO

Industry/Entity Type

Retail

Contact Information for Business Card

website: www.velvtharborboutiques.example email: sales@velvetharborboutique.example
Delia Pruett & Nadine Kolb Owners

Font styles to use
Script

Colors
b768aa

Requirements
Must have
• COLORS ARE PURPLE BLACK AND GREY
Nice to have
• INFINITY SIGNING IN THE BACKGROUND

```html
<!DOCTYPE html>
<html lang="en">
<head>
<meta charset="utf-8">
<title>Velvet Harbor Boutique – Business Card</title>
<link href="https://fonts.googleapis.com/css2?family=Cinzel:wght@400;500&family=Raleway:wght@400;500&display=swap" rel="stylesheet">
<style>
  :root {
    --backdrop: #1e1e21;
    --royal-purple: #744a9e;
    --deep-purple: #66418e;
    --silver: #cbcacd;
    --ink: #060606;
    --paper-white: #f4f2f6;
  }
  html, body {
    margin: 0;
    width: 1200px;
    height: 1200px;
    overflow: hidden;
    background: var(--backdrop);
  }
  .canvas {
    position: relative;
    width: 1200px;
    height: 1200px;
  }
  .card {
    position: absolute;
    left: 150px;
    width: 900px;
    height: 514px;
    overflow: hidden;
    box-shadow: 0 10px 30px rgba(0,0,0,.5);
  }
  .card-front { top: 56px; background: var(--royal-purple); }
  .card-back  { top: 630px; background: var(--silver); }

  .card-shapes { position: absolute; inset: 0; }

  .brand-name {
    position: absolute;
    left: 0; right: 0;
    text-align: center;
    font-family: "Cinzel", serif;
    font-weight: 400;
    letter-spacing: 2px;
    line-height: 1.1;
    margin: 0;
  }
  .card-front .brand-name { top: 120px; color: var(--paper-white); font-size: 50px; }
  .card-back  .brand-name { top: 70px;  color: var(--royal-purple); font-size: 50px; }
  .brand-name .brand-sub {
    display: block;
    font-size: 20px;
    letter-spacing: 12px;
    margin-top: 10px;
  }
  .card-front .brand-name .brand-sub { color: var(--paper-white); }

  .front-band {
    position: absolute;
    left: 0; right: 0; bottom: 0;
    height: 120px;
    background: var(--ink);
    border-top: 3px solid #b9a3d3;
    display: flex;
    align-items: center;
    justify-content: center;
  }
  .website-line {
    font-family: "Raleway", sans-serif;
    color: var(--paper-white);
    font-size: 20px;
    letter-spacing: 5px;
  }

  .contact-list {
    position: absolute;
    left: 36px;
    top: 240px;
    margin: 0;
    padding: 0;
    list-style: none;
    font-family: "Raleway", sans-serif;
    font-size: 19px;
    color: var(--paper-white);
  }
  .contact-list li {
    display: flex;
    align-items: center;
    gap: 12px;
    height: 34px;
  }
  .contact-list .address { display: block; height: auto; line-height: 28px; margin-bottom: 8px; }
  .contact-icon { width: 24px; height: 24px; flex: none; }

  .person {
    position: absolute;
    right: 48px;
    top: 360px;
    text-align: right;
  }
  .person-name {
    font-family: "Cinzel", serif;
    font-size: 32px;
    color: #8a5bbd;
    letter-spacing: 1px;
    margin: 0;
  }
  .person-role {
    font-family: "Raleway", sans-serif;
    font-size: 22px;
    color: var(--paper-white);
    margin: 0;
  }
</style>
</head>
<body>
<main class="canvas">

  <section class="card card-front" aria-label="Card front">
    <h1 class="brand-name">VELVET HARBOR<span class="brand-sub">BOUTIQUE</span></h1>
    <div class="front-band">
      <span class="website-line">www.velvtharborboutiques.example</span>
    </div>
  </section>

  <section class="card card-back" aria-label="Card back">
    <svg class="card-shapes" width="900" height="514" viewBox="0 0 900 514" aria-hidden="true">
      <polygon points="0,225 540,225 620,470 0,470" fill="var(--deep-purple)"/>
      <polygon points="560,250 900,250 900,470 632,470" fill="var(--ink)"/>
    </svg>

    <h2 class="brand-name">VELVET HARBOR<span class="brand-sub">BOUTIQUE</span></h2>

    <ul class="contact-list">
      <li class="address">PO BOX 48 Linden Lane<br>2nd street Ashford</li>
      <li>
        <svg class="contact-icon" viewBox="0 0 24 24" aria-hidden="true">
          <circle cx="12" cy="12" r="11" fill="none" stroke="#ddd" stroke-width="1.5"/>
          <path d="M9 7c-1 1-1.5 2 0 5s3.5 4.5 5 5c1 .3 2-.5 2-1l-1.8-1.6-1.2.8c-1-.5-2.3-1.8-2.8-2.8l.8-1.2L9.5 7z" fill="#ddd"/>
        </svg>
        (555) 014-2238
      </li>
      <li>
        <svg class="contact-icon" viewBox="0 0 24 24" aria-hidden="true">
          <circle cx="12" cy="12" r="11" fill="none" stroke="#ddd" stroke-width="1.5"/>
          <rect x="6" y="8" width="12" height="8" fill="none" stroke="#ddd" stroke-width="1.4"/>
          <path d="M6 8l6 5 6-5" fill="none" stroke="#ddd" stroke-width="1.4"/>
        </svg>
        hello@velvetmail.example
      </li>
      <li>
        <svg class="contact-icon" viewBox="0 0 24 24" aria-hidden="true">
          <circle cx="12" cy="12" r="11" fill="none" stroke="#ddd" stroke-width="1.5"/>
          <circle cx="12" cy="12" r="6" fill="none" stroke="#ddd" stroke-width="1.2"/>
          <ellipse cx="12" cy="12" rx="2.6" ry="6" fill="none" stroke="#ddd" stroke-width="1.2"/>
          <path d="M6 12h12" stroke="#ddd" stroke-width="1.2"/>
        </svg>
        www.velvtharborboutiques.example
      </li>
    </ul>

    <div class="person">
      <p class="person-name">ROWAN HALE</p>
      <p class="person-role">Founder</p>
    </div>
  </section>

</main>
</body>
</html>
```